VelTrova an innovative way to connect sellers with car dealers

The idea is a site that connects consumers that want to sell thier cars with a dealer network that is ready to buy.

**I just added 9/26 a POSSIBLE logo. Dont feel obligated to use this or design off of it.

The first goal is to provide a place where people can SEAMLESSLY list their vechile for sale to a car dealership network. We are looking for people that want to get more for their car than trading it in allows but DONT want to go through the hassel of listing and selling their car on their own. The dont want to deal with people reaching out, showing the vechile, and the risk assocated with retailing a valuable item to the general public. That said these people dont want to just trade their car wholesale and buy retail. These are the people that that do to a place like AutoPlenz to sell their car directly. However AutoPlenz is just one dealer.

The second fuction of the site allows dealers to view the vechiles that have been listed especilaly the ones in thier market.

I would like to add that I am looking for real images. No cartoon or animation. Upmarket but friendly.

I have attached a detailed document to help.

Target Market(s)

People that want to sell cars and dealers that want to buy cars

Industry/Entity Type

Automotive

Requirements
Must have
• The pages listed in the document
Should not have
• No cartoon or animated images

```html
<!DOCTYPE html>
<html lang="en">
<head>
<meta charset="utf-8">
<title>VelTrova — Sell Your Car Hassle Free</title>
<link rel="stylesheet" href="https://fonts.googleapis.com/css2?family=Plus+Jakarta+Sans:wght@400;500;600;700;800&display=swap">
<style>
:root{
  --red:#cc1417;
  --red-dark:#9e0f12;
  --ink:#111;
  --text:#333;
  --muted:#8a8a8a;
  --line:#ececec;
  --soft:#f7f7f8;
  --white:#fff;
}
*{box-sizing:border-box;margin:0;padding:0}
html,body{width:1200px;height:2799px;overflow:hidden}
body{position:relative;font-family:"Plus Jakarta Sans",sans-serif;color:var(--text);background:var(--white)}
.abs{position:absolute}

/* top bar */
.topbar{left:0;top:0;width:1200px;height:30px;background:var(--red);z-index:3}
.topbar .social{position:absolute;left:160px;top:8px;display:flex;gap:11px}
.dot{width:13px;height:13px;border-radius:50%;background:var(--white);opacity:.9}
.dot.active{border-radius:2px;background:var(--red-dark);width:20px;height:20px;margin-top:-3px}
.topbar .contact{position:absolute;right:152px;top:8px;color:var(--white);font-size:11px;font-weight:600;display:flex;gap:20px;align-items:center}
.topbar .contact span{display:flex;align-items:center;gap:6px}

/* nav */
.nav{left:150px;top:30px;width:900px;height:63px;background:var(--white);border-radius:0 0 6px 6px;z-index:3}
.brand{position:absolute;left:18px;top:14px;font-size:29px;font-weight:800;color:var(--ink);letter-spacing:-.3px}
.menu{position:absolute;left:290px;top:19px;display:flex;gap:12px;font-size:10px;font-weight:600;color:#444}
.menu a{padding:7px 12px;border-radius:3px;text-decoration:none;color:inherit}
.menu a.on{background:var(--red);color:var(--white)}
.search{position:absolute;left:633px;top:18px;width:248px;height:29px;border:1px solid #ddd;border-radius:4px;font-size:9px;color:#aaa;padding:9px 12px}
.search .go{position:absolute;right:2px;top:2px;width:27px;height:23px;border-radius:4px;background:#555}

/* hero */
.hero-art{left:0;top:0;width:1200px;height:632px}
.hero-title{left:0;top:240px;width:1200px;text-align:center;color:var(--white);font-size:52px;font-weight:800;line-height:56px;text-transform:uppercase;letter-spacing:-.5px}
.hero-title em{font-style:normal;color:var(--red)}
.btn{display:inline-block;font-size:11px;font-weight:600;text-transform:uppercase;text-align:center}
.hero-btn{left:520px;top:370px;width:159px;height:32px;line-height:32px;background:var(--white);color:var(--ink);border-radius:2px}

/* stats */
.stat{top:710px;width:200px;text-align:center}
.stat svg{display:block;margin:0 auto}
.stat .num{font-size:29px;font-weight:800;color:var(--red);margin-top:8px;line-height:32px}
.stat .lbl{font-size:13px;color:var(--ink);margin-top:2px}
.divider{left:150px;top:878px;width:900px;height:1px;background:var(--line)}

/* deals */
.section-title{left:0;top:948px;width:1200px;text-align:center;font-size:23px;font-weight:800;color:var(--red)}
.card{width:283px;height:337px;border:1px solid var(--line);background:var(--white)}
.card.raised{box-shadow:0 6px 18px rgba(0,0,0,.12)}
.card .photo{position:absolute;left:3px;top:3px;width:277px;height:162px}
.card .body{position:absolute;left:18px;top:182px;right:18px}
.card .cat{font-size:11px;color:var(--red)}
.card .name{font-size:13.5px;font-weight:700;color:var(--ink);margin-top:3px}
.card .price{font-size:11px;color:var(--red);margin-top:5px}
.specs{display:flex;gap:10px;margin-top:12px;padding-bottom:13px;border-bottom:1px solid var(--line)}
.spec{display:flex;gap:5px;font-size:9.5px;color:var(--ink);line-height:13px}
.spec small{display:block;color:var(--muted);font-size:9px}
.view{margin-top:18px;margin-left:13px;font-size:9.5px;font-weight:600;color:var(--muted);display:flex;align-items:center;gap:8px}
.card.raised .view{color:var(--red)}
.more{left:520px;top:1735px;width:141px;height:34px;line-height:32px;border:1px solid #ddd;color:var(--ink)}

/* testimonial */
.quote-bg{left:0;top:1830px;width:1200px;height:460px}
.stars{left:235px;top:1928px;display:flex;gap:3px;align-items:center;font-size:11px;color:#666}
.quote{left:235px;top:1966px;width:540px;font-size:20.5px;line-height:24px;color:#222}
.quote-rule{left:235px;top:2109px;width:515px;height:1px;background:#ddd}
.author{left:235px;top:2125px;display:flex;gap:12px;align-items:center}
.author b{display:block;color:var(--red);font-size:13px}
.author span{font-size:10.5px;color:var(--ink)}
.pager{left:168px;top:2018px;display:flex;flex-direction:column;gap:7px}
.pager i{width:10px;height:10px;border:1px solid #f0b8b9;border-radius:50%}
.pager i.on{background:var(--red);border-color:var(--red)}
.portrait-ring{left:807px;top:1938px;width:212px;height:212px;border-radius:50%;border:3px solid #f5d6d7;background:var(--white)}
.portrait{left:816px;top:1947px;width:194px;height:194px;border-radius:50%}

/* cta */
.cta-title{left:300px;top:2348px;width:385px;text-align:center;font-size:28px;font-weight:800;color:var(--ink);line-height:32px;text-transform:uppercase}
.cta-btn{left:728px;top:2365px;width:159px;height:32px;line-height:32px;background:var(--red);color:var(--white);border-radius:2px}

/* footer */
.footer-bg{left:0;top:2455px;width:1200px;height:344px}
.f-brand{left:150px;top:2570px;font-size:28px;font-weight:800;color:var(--white)}
.f-about{left:150px;top:2625px;width:180px;font-size:9.5px;line-height:13px;color:var(--white)}
.f-more{left:150px;top:2705px;font-size:9.5px;color:var(--red-dark);text-decoration:underline}
.f-head{top:2566px;font-size:15px;font-weight:700;color:var(--white)}
.f-list{font-size:11px;color:var(--white);line-height:13px}
.f-list li{list-style:none;display:flex;gap:9px;margin-bottom:13px}
.f-links li{margin-bottom:8px}
.f-links li.cur{color:var(--red-dark)}
.news{left:810px;top:2602px;width:240px;font-size:10.5px;color:var(--white);line-height:13px}
.email{left:810px;top:2640px;width:236px;height:26px;border-bottom:1px solid rgba(255,255,255,.5);font-size:10.5px;color:var(--white);display:flex;gap:10px;align-items:center;padding-left:8px}
.submit{left:809px;top:2680px;width:97px;height:29px;line-height:29px;background:var(--white);color:var(--ink)}
.bottom{left:0;top:2767px;width:1200px;height:32px;background:var(--red-dark);color:var(--white);font-size:10.5px}
.bottom p{position:absolute;left:152px;top:10px}
.bottom .social{position:absolute;right:153px;top:10px;display:flex;gap:12px}
</style>
</head>
<body>

<!-- hero -->
<svg class="abs hero-art" viewBox="0 0 1200 632" role="img" aria-label="Photograph of two women reviewing a car listing on a tablet in a dealership office">
  <defs>
    <linearGradient id="heroShade" x1="0" y1="0" x2="1" y2="1">
      <stop offset="0" stop-color="#5b6572"/>
      <stop offset=".5" stop-color="#3d4148"/>
      <stop offset="1" stop-color="#26292e"/>
    </linearGradient>
  </defs>
  <polygon points="0,0 1200,0 1200,541 0,571" fill="url(#heroShade)"/>
  <polygon points="0,571 1200,541 1200,588 0,632" fill="var(--red)"/>
  <polygon points="0,612 1200,573 1200,588 0,632" fill="var(--red-dark)"/>
</svg>

<div class="abs topbar">
  <div class="social"><i class="dot"></i><i class="dot"></i><i class="dot active"></i><i class="dot"></i></div>
  <div class="contact">
    <span><svg width="11" height="11" viewBox="0 0 24 24" fill="#fff"><path d="M6.6 10.8a15 15 0 006.6 6.6l2.2-2.2a1 1 0 011-.25 11.4 11.4 0 003.6.57 1 1 0 011 1V20a1 1 0 01-1 1A17 17 0 013 4a1 1 0 011-1h3.5a1 1 0 011 1c0 1.25.2 2.45.57 3.6a1 1 0 01-.25 1z"/></svg>555.010.2048</span>
    <span><svg width="12" height="10" viewBox="0 0 24 18" fill="#fff"><path d="M0 2l12 8 12-8V0H0zm0 3v13h24V5l-12 8z"/></svg>sales@veltrova.com</span>
  </div>
</div>

<header class="abs nav">
  <div class="brand">VELTROVA</div>
  <nav class="menu"><a class="on">HOME</a><a>WHAT WE DO</a><a>SIGN IN</a><a>DEALERSHIP LOGIN</a></nav>
  <div class="search">Search by make, model, or keyword
    <span class="go"><svg width="27" height="23" viewBox="0 0 27 23"><circle cx="14.5" cy="10.5" r="4" fill="none" stroke="#fff" stroke-width="1.3"/><line x1="11.5" y1="13.5" x2="9" y2="16" stroke="#fff" stroke-width="1.3"/></svg></span>
  </div>
</header>

<h1 class="abs hero-title"><em>Sell</em> your car<br>hassle <em>free</em></h1>
<span class="abs btn hero-btn">Sell your car now</span>

<!-- stats -->
<div class="abs stat" style="left:196px">
  <svg width="52" height="40" viewBox="0 0 52 40" fill="none" stroke="#222" stroke-width="2"><path d="M12 6h28l5 12H7z"/><rect x="4" y="18" width="44" height="12" rx="2"/><rect x="8" y="30" width="6" height="6"/><rect x="38" y="30" width="6" height="6"/><circle cx="12" cy="24" r="2.5" fill="var(--red)" stroke="none"/><circle cx="40" cy="24" r="2.5" fill="var(--red)" stroke="none"/><line x1="18" y1="24" x2="34" y2="24" stroke="var(--red)"/></svg>
  <div class="num">1856</div><div class="lbl">Vehicle in stock cars</div>
</div>
<div class="abs stat" style="left:416px">
  <svg width="44" height="40" viewBox="0 0 44 40" fill="none" stroke="#222" stroke-width="2"><rect x="4" y="1" width="36" height="10" rx="2" fill="var(--red)" stroke="none"/><circle cx="22" cy="19" r="4"/><circle cx="11" cy="21" r="3.5"/><circle cx="33" cy="21" r="3.5"/><path d="M14 37v-5a8 8 0 0116 0v5M3 37v-4a8 8 0 0110-6M41 37v-4a8 8 0 00-10-6"/></svg>
  <div class="num">1485</div><div class="lbl">Satisfied customers</div>
</div>
<div class="abs stat" style="left:623px">
  <svg width="40" height="40" viewBox="0 0 40 40" fill="none" stroke="#222" stroke-width="2"><path d="M10 3h20v12a10 10 0 01-20 0z"/><path d="M10 7H4a6 6 0 006 8M30 7h6a6 6 0 01-6 8"/><line x1="20" y1="25" x2="20" y2="31"/><rect x="12" y="31" width="16" height="6"/><circle cx="20" cy="13" r="4" fill="var(--red)" stroke="none"/></svg>
  <div class="num">65+</div><div class="lbl">Award achievement</div>
</div>
<div class="abs stat" style="left:818px">
  <svg width="48" height="38" viewBox="0 0 48 38" fill="none" stroke="#222" stroke-width="2"><path d="M4 36V4l40 14v18z"/><line x1="4" y1="36" x2="46" y2="36"/><rect x="14" y="20" width="14" height="9" fill="var(--red)" stroke="none"/><line x1="10" y1="8" x2="10" y2="36"/></svg>
  <div class="num">10+</div><div class="lbl">Total showroom</div>
</div>
<div class="abs divider"></div>

<!-- deals -->
<h2 class="abs section-title">Find The Best Deals</h2>

<!-- row 1 -->
<article class="abs card" style="left:150px;top:1002px">
  <div class="photo" role="img" aria-label="Photograph of a grey sedan parked outside a house" style="background:linear-gradient(160deg,#cfd3d6,#7d828a 60%,#4b4f55)"></div>
  <div class="body"><div class="cat">Sedan</div><div class="name">Norvane S3 Hybrid 2023</div><div class="price">$44,900</div>
    <div class="specs"><div class="spec"><svg width="12" height="14" viewBox="0 0 12 14" fill="none" stroke="#d88" stroke-width="1"><rect x="1" y="1" width="7" height="12"/><path d="M8 5h2v6"/></svg><div><small>Fuel type</small>Hybrid</div></div><div class="spec"><svg width="14" height="14" viewBox="0 0 14 14" fill="none" stroke="#d88" stroke-width="1"><path d="M2 11a6 6 0 1110 0"/><line x1="7" y1="8" x2="10" y2="5"/></svg><div><small>Mileage</small>15000 km</div></div><div class="spec"><svg width="14" height="14" viewBox="0 0 14 14" fill="none" stroke="#d88" stroke-width="1"><circle cx="2" cy="2" r="1.3"/><circle cx="7" cy="2" r="1.3"/><circle cx="12" cy="2" r="1.3"/><circle cx="2" cy="12" r="1.3"/><circle cx="7" cy="12" r="1.3"/><path d="M2 3v8M7 3v8M12 3v4H2"/></svg><div><small>Transmission</small>Auto</div></div></div>
    <div class="view">VIEW DETAILS <svg width="14" height="6" viewBox="0 0 14 6" fill="none" stroke="currentColor"><path d="M0 3h13M10 0l3 3-3 3"/></svg></div></div>
</article>
<article class="abs card" style="left:459px;top:1002px">
  <div class="photo" role="img" aria-label="Photograph of a red coupe on a track at sunset" style="background:linear-gradient(160deg,#c07048,#8a2a1e 55%,#3a3432)"></div>
  <div class="body"><div class="cat">Convertible</div><div class="name">Lumera GT Hybrid 2024</div><div class="price">$101,750</div>
    <div class="specs"><div class="spec"><svg width="12" height="14" viewBox="0 0 12 14" fill="none" stroke="#d88" stroke-width="1"><rect x="1" y="1" width="7" height="12"/><path d="M8 5h2v6"/></svg><div><small>Fuel type</small>Hybrid</div></div><div class="spec"><svg width="14" height="14" viewBox="0 0 14 14" fill="none" stroke="#d88" stroke-width="1"><path d="M2 11a6 6 0 1110 0"/><line x1="7" y1="8" x2="10" y2="5"/></svg><div><small>Mileage</small>15000 km</div></div><div class="spec"><svg width="14" height="14" viewBox="0 0 14 14" fill="none" stroke="#d88" stroke-width="1"><circle cx="2" cy="2" r="1.3"/><circle cx="7" cy="2" r="1.3"/><circle cx="12" cy="2" r="1.3"/><circle cx="2" cy="12" r="1.3"/><circle cx="7" cy="12" r="1.3"/><path d="M2 3v8M7 3v8M12 3v4H2"/></svg><div><small>Transmission</small>Cvt</div></div></div>
    <div class="view">VIEW DETAILS <svg width="14" height="6" viewBox="0 0 14 6" fill="none" stroke="currentColor"><path d="M0 3h13M10 0l3 3-3 3"/></svg></div></div>
</article>
<article class="abs card" style="left:767px;top:1002px">
  <div class="photo" role="img" aria-label="Photograph of a bright red sports sedan in front of trees" style="background:linear-gradient(170deg,#8ea27a,#5c6f4c 40%,#d41d1d 62%,#7a7a76)"></div>
  <div class="body"><div class="cat">Sedan</div><div class="name">Kestra TX Sport Edition</div><div class="price">$49,986</div>
    <div class="specs"><div class="spec"><svg width="12" height="14" viewBox="0 0 12 14" fill="none" stroke="#d88" stroke-width="1"><rect x="1" y="1" width="7" height="12"/><path d="M8 5h2v6"/></svg><div><small>Fuel type</small>Hybrid</div></div><div class="spec"><svg width="14" height="14" viewBox="0 0 14 14" fill="none" stroke="#d88" stroke-width="1"><path d="M2 11a6 6 0 1110 0"/><line x1="7" y1="8" x2="10" y2="5"/></svg><div><small>Mileage</small>15000 km</div></div><div class="spec"><svg width="14" height="14" viewBox="0 0 14 14" fill="none" stroke="#d88" stroke-width="1"><circle cx="2" cy="2" r="1.3"/><circle cx="7" cy="2" r="1.3"/><circle cx="12" cy="2" r="1.3"/><circle cx="2" cy="12" r="1.3"/><circle cx="7" cy="12" r="1.3"/><path d="M2 3v8M7 3v8M12 3v4H2"/></svg><div><small>Transmission</small>Auto</div></div></div>
    <div class="view">VIEW DETAILS <svg width="14" height="6" viewBox="0 0 14 6" fill="none" stroke="currentColor"><path d="M0 3h13M10 0l3 3-3 3"/></svg></div></div>
</article>

<!-- row 2 -->
<article class="abs card" style="left:150px;top:1366px">
  <div class="photo" role="img" aria-label="Photograph of a dark blue sedan among palm trees" style="background:linear-gradient(165deg,#7c8a6a,#3b3f4a 45%,#1d2640 65%,#8a8680)"></div>
  <div class="body"><div class="cat">Sedan</div><div class="name">Norvane S3 Hybrid 2023</div><div class="price">$44,900</div>
    <div class="specs"><div class="spec"><svg width="12" height="14" viewBox="0 0 12 14" fill="none" stroke="#d88" stroke-width="1"><rect x="1" y="1" width="7" height="12"/><path d="M8 5h2v6"/></svg><div><small>Fuel type</small>Hybrid</div></div><div class="spec"><svg width="14" height="14" viewBox="0 0 14 14" fill="none" stroke="#d88" stroke-width="1"><path d="M2 11a6 6 0 1110 0"/><line x1="7" y1="8" x2="10" y2="5"/></svg><div><small>Mileage</small>15000 km</div></div><div class="spec"><svg width="14" height="14" viewBox="0 0 14 14" fill="none" stroke="#d88" stroke-width="1"><circle cx="2" cy="2" r="1.3"/><circle cx="7" cy="2" r="1.3"/><circle cx="12" cy="2" r="1.3"/><circle cx="2" cy="12" r="1.3"/><circle cx="7" cy="12" r="1.3"/><path d="M2 3v8M7 3v8M12 3v4H2"/></svg><div><small>Transmission</small>Auto</div></div></div>
    <div class="view">VIEW DETAILS <svg width="14" height="6" viewBox="0 0 14 6" fill="none" stroke="currentColor"><path d="M0 3h13M10 0l3 3-3 3"/></svg></div></div>
</article>
<article class="abs card" style="left:459px;top:1366px">
  <div class="photo" role="img" aria-label="Photograph of a white coupe in a dark studio" style="background:radial-gradient(ellipse at 55% 60%,#e8e8e8 0,#9a9a9a 30%,#1e1e1e 70%)"></div>
  <div class="body"><div class="cat">Convertible</div><div class="name">Lumera GT Hybrid 2024</div><div class="price">$101,750</div>
    <div class="specs"><div class="spec"><svg width="12" height="14" viewBox="0 0 12 14" fill="none" stroke="#d88" stroke-width="1"><rect x="1" y="1" width="7" height="12"/><path d="M8 5h2v6"/></svg><div><small>Fuel type</small>Hybrid</div></div><div class="spec"><svg width="14" height="14" viewBox="0 0 14 14" fill="none" stroke="#d88" stroke-width="1"><path d="M2 11a6 6 0 1110 0"/><line x1="7" y1="8" x2="10" y2="5"/></svg><div><small>Mileage</small>15000 km</div></div><div class="spec"><svg width="14" height="14" viewBox="0 0 14 14" fill="none" stroke="#d88" stroke-width="1"><circle cx="2" cy="2" r="1.3"/><circle cx="7" cy="2" r="1.3"/><circle cx="12" cy="2" r="1.3"/><circle cx="2" cy="12" r="1.3"/><circle cx="7" cy="12" r="1.3"/><path d="M2 3v8M7 3v8M12 3v4H2"/></svg><div><small>Transmission</small>Cvt</div></div></div>
    <div class="view">VIEW DETAILS <svg width="14" height="6" viewBox="0 0 14 6" fill="none" stroke="currentColor"><path d="M0 3h13M10 0l3 3-3 3"/></svg></div></div>
</article>
<article class="abs card raised" style="left:767px;top:1366px">
  <div class="photo" role="img" aria-label="Photograph of a bright blue sports sedan in a grey studio" style="background:linear-gradient(165deg,#d6d9dc,#9aa0a6 35%,#1f6ad6 60%,#5a6068)"></div>
  <div class="body"><div class="cat">Sedan</div><div class="name">Kestra TX Sport Edition</div><div class="price">$49,986</div>
    <div class="specs"><div class="spec"><svg width="12" height="14" viewBox="0 0 12 14" fill="none" stroke="#d88" stroke-width="1"><rect x="1" y="1" width="7" height="12"/><path d="M8 5h2v6"/></svg><div><small>Fuel type</small>Hybrid</div></div><div class="spec"><svg width="14" height="14" viewBox="0 0 14 14" fill="none" stroke="#d88" stroke-width="1"><path d="M2 11a6 6 0 1110 0"/><line x1="7" y1="8" x2="10" y2="5"/></svg><div><small>Mileage</small>15000 km</div></div><div class="spec"><svg width="14" height="14" viewBox="0 0 14 14" fill="none" stroke="#d88" stroke-width="1"><circle cx="2" cy="2" r="1.3"/><circle cx="7" cy="2" r="1.3"/><circle cx="12" cy="2" r="1.3"/><circle cx="2" cy="12" r="1.3"/><circle cx="7" cy="12" r="1.3"/><path d="M2 3v8M7 3v8M12 3v4H2"/></svg><div><small>Transmission</small>Auto</div></div></div>
    <div class="view">VIEW DETAILS <svg width="14" height="6" viewBox="0 0 14 6" fill="none" stroke="currentColor"><path d="M0 3h13M10 0l3 3-3 3"/></svg></div></div>
</article>

<span class="abs btn more">More listings</span>

<!-- testimonial -->
<svg class="abs quote-bg" viewBox="0 0 1200 460"><polygon points="0,18 1200,4 1200,437 0,454" fill="var(--soft)"/></svg>
<div class="abs stars">
  <svg width="92" height="15" viewBox="0 0 92 15" fill="var(--red)"><g id="star"><path d="M7.5 0l2.2 4.8 5.3.6-3.9 3.6 1 5.2-4.6-2.6-4.6 2.6 1-5.2L0 5.4l5.3-.6z"/></g><use href="#star" x="18.5"/><use href="#star" x="37"/><use href="#star" x="55.5"/><path d="M81.5 0l2.2 4.8 5.3.6-3.9 3.6 1 5.2-4.6-2.6-4.6 2.6 1-5.2L74 5.4l5.3-.6z" fill="none" stroke="var(--red)" stroke-width="1.5"/></svg>
  <span style="margin-left:6px">4.5</span>
</div>
<p class="abs quote">Lorem Ipsum is simply dummy text of the printing and typesetting industry. Lorem Ipsum has been the industry's standard dummy text ever since the 1500s, when an unknown printer took a galley of type and scrambled it to make a type specimen book.</p>
<div class="abs pager"><i></i><i></i><i class="on"></i><i></i></div>
<div class="abs quote-rule"></div>
<div class="abs author">
  <svg width="46" height="38" viewBox="0 0 46 38" fill="none" stroke="var(--red)" stroke-width="1.5"><path d="M10 2C4 14 2 20 2 26a9 9 0 0018 0c0-6-4-9-9-9M32 2c-6 12-8 18-8 24a9 9 0 0018 0c0-6-4-9-9-9"/></svg>
  <div><b>Daniel Rowe</b><span>Head of Data and AI at Travelnest</span></div>
</div>
<div class="abs portrait-ring"></div>
<div class="abs portrait" role="img" aria-label="Portrait photograph of the reviewer" style="background:radial-gradient(circle at 50% 40%,#e6ecef,#b9c4cb)"></div>

<!-- call to action -->
<h2 class="abs cta-title">Do you have something to sell through us?</h2>
<span class="abs btn cta-btn">Sell your car now</span>

<!-- footer -->
<svg class="abs footer-bg" viewBox="0 0 1200 344"><polygon points="0,68 1200,0 1200,344 0,344" fill="var(--red-dark)"/><polygon points="0,68 1200,28 1200,344 0,344" fill="var(--red)"/></svg>
<div class="abs f-brand">VELTROVA</div>
<p class="abs f-about">Lorem Ipsum is simply dummy text of the printing and typesetting industry. Lorem Ipsum has been the industry's standard dummy text ever since the 1500s, when an unknown...</p>
<span class="abs f-more">Readmore</span>

<h3 class="abs f-head" style="left:388px">Conatct info</h3>
<ul class="abs f-list" style="left:388px;top:2602px;width:210px">
  <li><svg width="12" height="14" viewBox="0 0 12 14" fill="var(--red-dark)"><path d="M6 0a5 5 0 015 5c0 4-5 9-5 9S1 9 1 5a5 5 0 015-5z"/><circle cx="6" cy="5" r="2" fill="var(--red)"/></svg><span>Lorem Ipsum, Pinefield 10482<br>United States</span></li>
  <li><svg width="12" height="12" viewBox="0 0 24 24" fill="var(--red-dark)"><path d="M6.6 10.8a15 15 0 006.6 6.6l2.2-2.2a1 1 0 011-.25 11.4 11.4 0 003.6.57 1 1 0 011 1V20a1 1 0 01-1 1A17 17 0 013 4a1 1 0 011-1h3.5a1 1 0 011 1c0 1.25.2 2.45.57 3.6a1 1 0 01-.25 1z"/></svg><span>1-800-555-0142</span></li>
  <li><svg width="12" height="10" viewBox="0 0 24 18" fill="var(--red-dark)"><path d="M0 2l12 8 12-8V0H0zm0 3v13h24V5l-12 8z"/></svg><span>info@veltrova.com</span></li>
  <li><svg width="12" height="12" viewBox="0 0 12 12" fill="none" stroke="var(--red-dark)" stroke-width="1.5"><circle cx="6" cy="6" r="5"/><path d="M1 6h10M6 1c-3 3-3 7 0 10M6 1c3 3 3 7 0 10"/></svg><span>Live location</span></li>
</ul>

<h3 class="abs f-head" style="left:636px">Quick Link</h3>
<ul class="abs f-list f-links" style="left:636px;top:2602px">
  <li class="cur">Home</li><li>What we do</li><li>Sign in</li><li>Dealership Login</li><li>Contact Us</li>
</ul>

<h3 class="abs f-head" style="left:810px">Stay In Touch</h3>
<p class="abs news">Subscribe to our newsletter and<br>stay updated</p>
<div class="abs email"><svg width="14" height="14" viewBox="0 0 14 14" fill="none" stroke="#fff" stroke-width="1.2"><circle cx="7" cy="7" r="2.5"/><path d="M9.5 7v1.2a1.8 1.8 0 003.6 0V7A6 6 0 107 13"/></svg>Your email address*</div>
<span class="abs btn submit">Submit</span>

<footer class="abs bottom">
  <p>© 2024 VelTrova. All Right Reserved</p>
  <div class="social"><i class="dot"></i><i class="dot"></i><i class="dot active" style="background:var(--red)"></i><i class="dot"></i></div>
</footer>

</body>
</html>
```